Sphynx Cat Breeder

Hi.
I have just got a logo through Pixel Harbor, and now I need a website.
I am home based Sphynx cat breeder (Plumwick Sphynx)
I want to be able to show my breedings cats and kittens available for sale on my website.

Target Market(s)

Buyers of pet kittens in New Zealand, plus potentially buyers of kittens for breeding for overseas breeders

Requirements
Must have
• Home page
About Us
My breeding Cats
Kittens
Caring for a Sphynx
Links
Contact (contact details plus a link to email)
I need to be able to upload photos as kittens come and go.
Nice to have
• A web counter, visible only to me, preferably showing which country they are from

```html
<!DOCTYPE html>
<html lang="en">
<head>
<meta charset="utf-8">
<title>Plumwick Sphynx – Home</title>
<link rel="stylesheet" href="https://fonts.googleapis.com/css2?family=Arimo:wght@400;700&family=Tinos:wght@400;700&display=swap">
<style>
  :root {
    --ink: #1c1c1c;
    --nav-bg: #141414;
    --nav-text: #f2f2f2;
    --nav-sep: #777777;
    --bg-dark: #4e4e4e;
    --bg-mid: #9a9a9a;
    --bg-light: #f1f1f1;
    --copy: #ffffff;
    --link: #8fd0f2;
    --footer-stripe: #8a8a8a;
    --footer-bg: #2a2a2a;
    --footer-text: #d8d8d8;
  }
  * { box-sizing: border-box; margin: 0; padding: 0; }
  html, body { width: 1200px; height: 900px; overflow: hidden; }
  body {
    position: relative;
    font-family: "Arimo", Arial, sans-serif;
    background:
      radial-gradient(ellipse 700px 620px at 860px 470px, rgba(255,255,255,0.85), rgba(255,255,255,0) 70%),
      linear-gradient(90deg, var(--bg-dark) 0%, var(--bg-mid) 38%, #cfcfcf 60%, var(--bg-light) 100%);
  }

  .site-nav {
    position: absolute; top: 0; left: 413px; right: 0; height: 33px;
    background: var(--nav-bg);
    border-bottom-left-radius: 26px;
    display: flex; align-items: center; justify-content: flex-end;
    padding-right: 14px;
  }
  .site-nav a {
    color: var(--nav-text); text-decoration: none;
    font-size: 13px; padding: 0 16px; position: relative;
  }
  .site-nav a + a::before {
    content: ""; position: absolute; left: 0; top: 3px; width: 1px; height: 11px;
    background: var(--nav-sep);
  }

  .brand {
    position: absolute; left: 80px; top: 110px;
    display: flex; align-items: center; gap: 14px;
  }
  .brand-dot { width: 34px; height: 34px; border-radius: 50%; background: var(--ink); }
  .brand-name {
    font-family: "Tinos", "Times New Roman", serif; font-weight: 700;
    font-size: 30px; color: var(--ink);
  }

  .headline {
    position: absolute; left: 70px; top: 336px; width: 480px; height: 116px;
    display: flex; align-items: center; justify-content: space-between;
    font-family: "Tinos", "Times New Roman", serif;
  }
  .headline .brace { font-size: 120px; line-height: 1; color: var(--ink); font-weight: 400; margin-top: -18px; }
  .headline h1 {
    font-size: 34px; font-weight: 400; color: #ffffff;
    text-shadow: 1px 1px 2px rgba(0,0,0,0.55);
  }

  .intro {
    position: absolute; left: 110px; top: 488px; width: 410px;
    color: var(--copy); font-size: 13px; line-height: 16px;
  }
  .intro p + p { margin-top: 16px; }
  .intro a { color: var(--link); text-decoration: none; margin-left: 6px; }

  .kitten-thumbs {
    position: absolute; left: 110px; top: 646px;
    display: flex; gap: 12px;
  }
  .thumb {
    width: 91px; height: 91px; border-radius: 3px;
    box-shadow: 0 2px 5px rgba(0,0,0,0.45);
  }
  .thumb-1 { background: linear-gradient(150deg, #f1efef, #c9c4c4 60%, #8d8a8a); }
  .thumb-2 { background: linear-gradient(150deg, #6a5f5b, #a99690 55%, #d6c7c2); }
  .thumb-3 { background: linear-gradient(150deg, #3a3a3a, #9b9a9a 50%, #d9d8d8); }
  .thumb-4 { background: linear-gradient(150deg, #e5dcd9, #a89e9b 55%, #5b5656); }

  .order-button {
    position: absolute; left: 110px; top: 757px; width: 400px; height: 34px;
    background: linear-gradient(#555555, #1d1d1d 55%, #0e0e0e);
    border-radius: 3px; box-shadow: 0 2px 4px rgba(0,0,0,0.4);
    color: #ffffff; font-size: 15px; text-decoration: none;
    display: flex; align-items: center; padding-left: 34px;
  }

  .hero-kitten {
    position: absolute; left: 655px; top: 312px; width: 485px; height: 498px;
    border-radius: 46% 46% 40% 40%;
    background: radial-gradient(ellipse at 55% 45%, #8b7a73 0%, #776863 40%, rgba(160,150,146,0.6) 70%, rgba(230,230,230,0) 100%);
  }

  .site-footer {
    position: absolute; left: 0; right: 0; top: 881px; height: 19px;
    background: var(--footer-bg);
    border-top: 6px solid var(--footer-stripe);
    display: flex; align-items: center; justify-content: flex-end;
    padding-right: 8px;
  }
  .site-footer p { color: var(--footer-text); font-size: 11px; line-height: 1; }
</style>
</head>
<body>
  <nav class="site-nav">
    <a href="#">Home</a>
    <a href="#">About Us</a>
    <a href="#">Our Breeding Cats</a>
    <a href="#">Our Kittens</a>
    <a href="#">Gallery</a>
    <a href="#">Caring for your Sphynx</a>
    <a href="#">Links</a>
    <a href="#">Contact Us</a>
  </nav>

  <div class="brand">
    <span class="brand-dot"></span>
    <span class="brand-name">Plumwick Sphynx</span>
  </div>

  <header class="headline">
    <span class="brace">{</span>
    <h1>The Kittens Have Arrived</h1>
    <span class="brace">}</span>
  </header>

  <section class="intro">
    <p>Lorem ipsum dolor sit amet, consectetuer adipiscing elit, sed diam nonummy nibh euismod tincidunt ut laoreet dolore magna aliquam erat volutpat. Ut wisi enim ad minim veniam, quis a nostrud exerci tation ullamcorper suscipit lobortis nisl ut aliquip ex ea commodo.</p>
    <p>Duis autem vel eum iriure dolor in hendrerit in vulputate velit esse molestie consequat, vel illum dolore eu feugiat nulla facilisis vero.</p>
    <p>For all queries please contact us on: <a href="mailto:info@plumwicksphynx.com">info@plumwicksphynx.com</a></p>
  </section>

  <div class="kitten-thumbs">
    <div class="thumb thumb-1" role="img" aria-label="Photo of a pale sphynx kitten"></div>
    <div class="thumb thumb-2" role="img" aria-label="Photo of a grey and pink sphynx kitten"></div>
    <div class="thumb thumb-3" role="img" aria-label="Photo of a dark grey sphynx kitten"></div>
    <div class="thumb thumb-4" role="img" aria-label="Photo of a cream sphynx kitten"></div>
  </div>

  <a class="order-button" href="#">Place an order for your Sphynx Kitten today</a>

  <div class="hero-kitten" role="img" aria-label="Photo of a young sphynx kitten sitting and meowing"></div>

  <footer class="site-footer">
    <p>2012 © Plumwick Sphynx</p>
  </footer>
</body>
</html>
```